Captain Pebble - Book cover for a children's book

I need a book cover for a children's book size A 4 which can be used for print and ebook. The story has about 16,000 words and ten hand-made watercolor illustrations. One of these should be on the book cover (file provided). The design of the book cover should match the illustration.
The book is for children aged 6-10 years old.

Name of the book: Captain Pebble
written by: Tilda Vorhagen
illustrated by: Celeste Marina Dunn

Thank you!

Synopsis:
Captain Pebble is the story of a frustrated mouse who is the leader of a questing team, comprised of himself, a racoon, a slug, and a giraffe – Captain Pebble (ambitious, but with low self-esteem that he covers up by being bossy), Pippa Parrot (beautiful, forgetful, and unable to read), Wendy Worm (confident and strong, but extremely slow) and Oliver Otter (jolly and practical, yet single-mindedly focused on food). One of the many running jokes throughout the book is that Captain Pebble thinks Oliver is a pig, a confusion which is only resolved near the end of the book. Captain Pebble sees himself as the rightful leader of the team, as he is by far the smartest. He also fears he will not be successful in completing his quest, as he has been forced to team up with less than ideal quest teammates. During the team’s quest, Captain Pebble loses each of his team members, one by one. Following the revelation of her illiteracy, Pippa opts to stay behind at the first obstacle, Oliver runs off after apples for lunch, and Wendy gets distracted. Captain Pebble is excited to be able to go off on his own but gets snatched by an eagle. The other three team members band together to rescue Captain Pebble in haphazard circumstances. They all return to Quest school jubilant and ready to receive their diplomas, not realising that Captain Pebble will not qualify because he was the one who had to be rescued. When Captain Pebble does not get his diploma, the team come together and recall that during the rescue Captain Pebble had in fact also saved Wendy Worm, allowing them all to graduate together.
With so many different characteristics, the team show that they are stronger together than as individuals. By embracing their weaknesses and vulnerabilities they learn to cooperate and in the end this helps them to succeed. The team agree to stick together for future adventures.

Target Market(s)

Children 6-10 years old + their carers/grand-parents/ primary school teachers

Font styles to use
Serif
Sans Serif

Requirements
Must have
• Beautiful colors (matching the provided illustration), must have the provided illustration on the cover, must be appealing and heart-warming, spiking curiosity.

Must feature book name, name of author and name of illustrator.

Text for blurb on the back of the book cover:

"Captain Pebble tells the delightful story of four animals on a quest. These four could not be more different – there is a mouse, a giraffe, a slug, and a pig. But wait – is this really true? Captain Pebble, who thinks he is the leader, seems to have missed his zoology lessons at school.
There is more than one team competing to complete the quest. Can our odd team beat the lions? Who will be faster? Does being faster mean that you win? Find out what really matters in the end!"
Should not have
• should not be over-loaded, no large white spaces

```html
<!DOCTYPE html>
<html lang="en">
<head>
<meta charset="utf-8">
<title>Captain Pebble – Cover Spread</title>
<link rel="stylesheet" href="https://fonts.googleapis.com/css2?family=Pompiere&family=Nanum+Pen+Script&family=Ubuntu+Condensed&display=swap">
<style>
  :root {
    --stage: #636363;
    --ink: #1f2226;
    --ink-soft: #3a3d42;
    --sky: #bfeaf2;
    --sky-deep: #7fd6e6;
    --aqua: #2fd0da;
    --sun: #f8ef5a;
    --blush: #f7b6dc;
    --grass: #a9d46a;
    --giraffe: #e59a45;
    --rainbow: linear-gradient(100deg, #2a9ad8 0%, #7a3fc4 22%, #e5338f 42%, #f5a623 58%, #b9d636 74%, #22b9a8 100%);
  }
  * { margin: 0; padding: 0; box-sizing: border-box; }
  html, body { width: 973px; height: 1200px; overflow: hidden; }
  body { background: var(--stage); position: relative; }

  .spread {
    position: absolute;
    left: 37px; top: 291px;
    width: 900px; height: 617px;
    display: flex;
  }

  /* Back cover */
  .back-cover { position: relative; width: 436px; height: 100%; overflow: hidden; }
  .back-art {
    position: absolute; inset: 0;
    background:
      linear-gradient(180deg, transparent 78%, var(--grass) 100%),
      linear-gradient(90deg, var(--sun) 0%, #fbf7b0 10%, var(--blush) 24%, #c9f3f6 40%, var(--aqua) 62%, var(--sky) 80%, #e6f8fa 100%);
  }
  .back-title { position: absolute; left: 155px; top: 16px; font-family: "Pompiere", cursive; line-height: 1; }
  .back-title .word-one { display: block; font-size: 58px; }
  .back-title .word-two { display: block; font-size: 58px; margin-left: 50px; margin-top: -4px; }

  .rainbow-text {
    background: var(--rainbow);
    -webkit-background-clip: text; background-clip: text;
    color: transparent;
  }

  .blurb {
    position: absolute; left: 40px; right: 14px; top: 172px;
    font-family: "Nanum Pen Script", cursive;
    font-size: 21px; line-height: 22px;
    color: var(--ink); text-align: center;
  }

  /* Spine */
  .spine {
    position: relative; width: 29px; height: 100%;
    background: linear-gradient(180deg, #1fb7a6 0%, var(--aqua) 22%, #1aa7d8 42%, #d44fb8 64%, #f16c8d 78%, #f8a53b 90%, var(--sun) 100%);
  }
  .spine-text {
    position: absolute; left: 50%; white-space: nowrap;
    transform: translateX(-50%) rotate(90deg);
    transform-origin: center;
    font-family: "Ubuntu Condensed", sans-serif; font-size: 19px; color: var(--ink);
  }
  .spine-title { top: 112px; }
  .spine-author { top: 470px; }

  /* Front cover */
  .front-cover { position: relative; width: 435px; height: 100%; overflow: hidden; }
  .front-art {
    position: absolute; inset: 0;
    background:
      linear-gradient(180deg, transparent 82%, var(--grass) 100%),
      radial-gradient(ellipse 62% 48% at 38% 34%, var(--giraffe) 0%, #f0c070 45%, transparent 72%),
      linear-gradient(180deg, var(--sky-deep) 0%, var(--sky) 40%, #eefafb 80%);
  }
  .illustrator-credit {
    position: absolute; right: 28px; top: 22px;
    font-family: "Ubuntu Condensed", sans-serif; font-size: 10px; color: var(--ink-soft);
  }
  .front-title { position: absolute; left: 22px; top: 350px; font-family: "Pompiere", cursive; line-height: 1; }
  .front-title .word-one { display: block; font-size: 86px; }
  .front-title .word-two { display: block; font-size: 86px; margin-left: 72px; margin-top: -10px; }
  .author {
    position: absolute; left: 23px; top: 522px;
    font-family: "Ubuntu Condensed", sans-serif; font-size: 29px; color: var(--ink);
  }
</style>
</head>
<body>
  <main class="spread">
    <section class="back-cover">
      <div class="back-art" role="img" aria-label="Rainbow watercolour wash with a small mouse standing in grass and wildflowers"></div>
      <h2 class="back-title">
        <span class="word-one rainbow-text">Captain</span>
        <span class="word-two rainbow-text">Pebble</span>
      </h2>
      <p class="blurb">
        "Captain Pebble tells the delightful story of four animals on a quest.<br>
        These four could not be more different – there is a mouse, a giraffe, a slug, and a pig.<br>
        But wait – is this really true? Captain Pebble, who thinks he is the leader, seems to have missed his zoology lessons at school.<br>
        There is more than one team competing to complete the quest.<br>
        Can our odd team beat the lions? Who will be faster?<br>
        Does being faster mean that you win?<br>
        Find out what really matters in the end!"
      </p>
    </section>

    <section class="spine">
      <span class="spine-text spine-title">Captain Pebble</span>
      <span class="spine-text spine-author">Tilda Vorhagen</span>
    </section>

    <section class="front-cover">
      <div class="front-art" role="img" aria-label="Watercolour illustration of a giraffe looking down at a small mouse standing in the grass under a pale blue sky"></div>
      <p class="illustrator-credit">Illustrated by: Celeste Marina Dunn</p>
      <h1 class="front-title">
        <span class="word-one rainbow-text">Captain</span>
        <span class="word-two rainbow-text">Pebble</span>
      </h1>
      <p class="author">Tilda Vorhagen</p>
    </section>
  </main>
</body>
</html>
```